A5 Personal trainer profile for brackmoor wellness

I need a A5 Landscape profile designed for the company I work for. Company name is Brackmoor Wellness. The profile is for personal trainers to let people know:

1. Brief description of themselves
2. Qualifications

A picture will be required on the right hand side of the profile. Brackmoor Wellness colours are green and white.

The Brackmoor Wellness Logo in the boarder of the example included must remain. We are looking for a clinical and professional design.

Industry/Entity Type

Health

```html
<!DOCTYPE html>
<html lang="en">
<head>
<meta charset="utf-8">
<title>Personal Trainer Profile – Marcus Adjei – Brackmoor Wellness</title>
<link href="https://fonts.googleapis.com/css2?family=Oswald:wght@400;500;600&family=Montserrat:wght@400;500;700&display=swap" rel="stylesheet">
<style>
  :root {
    --green-deep: #1f7a3c;
    --green-mid: #3a9e44;
    --green-bright: #4db848;
    --ink: #1a1a1a;
    --paper: #ffffff;
    --photo-light: #f4f6f2;
    --photo-shirt: #9bd85f;
  }
  * { margin: 0; padding: 0; box-sizing: border-box; }
  html, body {
    width: 1200px; height: 846px; overflow: hidden;
    background: var(--paper);
  }
  .profile {
    position: relative; width: 1200px; height: 846px;
    background: var(--paper);
    font-family: "Montserrat", Arial, sans-serif;
    color: var(--ink);
  }
  .header-band {
    position: absolute; left: 0; top: 29px; width: 1200px; height: 164px;
    background: linear-gradient(90deg, var(--green-deep) 0%, var(--green-mid) 45%, var(--green-bright) 100%);
  }
  .role-title {
    position: absolute; left: 82px; top: 56px;
    font-family: "Oswald", "Arial Narrow", sans-serif; font-weight: 500;
    font-size: 30px; line-height: 1; color: var(--paper);
  }
  .trainer-name {
    position: absolute; left: 80px; top: 94px;
    font-family: "Oswald", "Arial Narrow", sans-serif; font-weight: 600;
    font-size: 74px; line-height: 1; letter-spacing: 1px; color: var(--paper);
  }
  .section-heading {
    position: absolute; left: 82px;
    font-weight: 700; font-size: 17.5px; line-height: 1;
  }
  .help-heading { top: 242px; text-transform: uppercase; }
  .qual-heading { top: 553px; }
  .bullet-list {
    position: absolute; left: 82px; list-style: none;
    font-size: 18px; line-height: 24.2px; font-weight: 400;
  }
  .bullet-list li { position: relative; padding-left: 16px; }
  .bullet-list li::before {
    content: ""; position: absolute; left: 1px; top: 10px;
    width: 6px; height: 6px; border-radius: 50%; background: var(--green-bright);
  }
  .help-list { top: 262px; }
  .qual-list { top: 574px; }
  .testimonial {
    position: absolute; left: 82px; top: 408px; width: 625px;
    font-family: "Oswald", "Arial Narrow", sans-serif; font-weight: 500;
    font-size: 22px; line-height: 29px; text-transform: uppercase;
    color: var(--green-bright);
  }
  .testimonial .mark {
    font-weight: 600; font-size: 40px; line-height: 0;
    vertical-align: -12px; margin-right: 2px;
  }
  .testimonial .mark.close { margin: 0 2px 0 1px; }
  .testimonial cite { font-style: normal; font-size: 13px; margin-left: 2px; }
  .photo-frame {
    position: absolute; left: 740px; top: 240px; width: 460px; height: 518px;
    border-left: 4px solid var(--green-bright); border-top: 4px solid var(--green-bright);
    background: linear-gradient(180deg, var(--photo-light) 0%, var(--photo-light) 50%, var(--photo-shirt) 78%, var(--photo-shirt) 100%);
  }
  .footer-rule {
    position: absolute; left: 0; top: 757px; width: 1200px; height: 8px;
    background: var(--green-bright);
  }
  .brand-mark {
    position: absolute; right: 63px; top: 796px;
    display: flex; align-items: center; gap: 6px;
    font-weight: 700; font-size: 17px; color: var(--green-mid);
  }
  .brand-mark .square { width: 14px; height: 14px; background: var(--green-mid); }
</style>
</head>
<body>
  <main class="profile">
    <header class="header-band"></header>
    <p class="role-title">Personal Trainer</p>
    <h1 class="trainer-name">MARCUS ADJEI</h1>

    <h2 class="section-heading help-heading">How can I help you?</h2>
    <ul class="bullet-list help-list">
      <li>Reduce body fat and increase body definition</li>
      <li>Increase stamina, improve agility and speed</li>
      <li>Increase strength and size</li>
      <li>Plyometric training and conditioning</li>
      <li>Flexibility and core strength</li>
    </ul>

    <blockquote class="testimonial">
      <span class="mark">“</span>With Marcus my training is always challenging and fun. I don’t remember a session to be boring or repetitive. In short time<br>I improved my core strength and flexibility. I can run 10k<br>without stopping. It is amazing improvement.<span class="mark close">”</span><cite>Laura Pennick</cite>
    </blockquote>

    <h2 class="section-heading qual-heading">Qualifications</h2>
    <ul class="bullet-list qual-list">
      <li>Advanced Circuit Training</li>
      <li>Advanced Diploma in Personal Training -<br>Level 3 NFPR Registered</li>
      <li>Fitness Instructor - Level 2 NFPR Registered</li>
      <li>Also qualified in – Suspension training, Studio Cycling,<br>Sports Nutrition, Weight Management</li>
    </ul>

    <div class="photo-frame" role="img" aria-label="Portrait photo of the personal trainer smiling, wearing a bright green polo shirt"></div>
    <div class="footer-rule"></div>

    <div class="brand-mark"><span class="square"></span>Brackmoor Wellness</div>
  </main>
</body>
</html>
```